Brochure for Company

We need a standard trifold brochure or a square trifold brochure design. We are a home medical equipment company that specializes in pediatric as well as prenatal and postnatal medical equipment (www.vorantiq.com). We are owned by a home care company called Bluestem Home Health (www.bluestemnurse.com) which specializes in pediatric home care. Our two main products are breast pumps and nebulizer compressor kits. However, we also carry other respiratory as well as pre and post natal products. We are looking a creative and simple design. Most of our competitors brochures are very cookie cutter and too wordy so I want to stray away from them. The design should communicate that we care about our clients, meaning children and parents.

I have added a bunch of images that could be used. I also included the type of brochure I would ideally want to use.

Reason: i'm travelling the next couple of days so i need more time to review the submissions.

Industry/Entity Type

Medical

```html
<!DOCTYPE html>
<html lang="en">
<head>
<meta charset="utf-8">
<title>Vorantiq Medical Products — Trifold Brochure</title>
<link rel="stylesheet" href="https://fonts.googleapis.com/css2?family=Lato:wght@300;400;700;900&display=swap">
<style>
  :root {
    --page-bg: #e6e6e6;
    --paper: #ffffff;
    --brand-blue: #1b4f9f;
    --band-blue: #1d4fa3;
    --band-light: #d4ebf7;
    --brand-orange: #f28a1d;
    --text-grey: #555a60;
    --fold-shade: rgba(0, 0, 0, 0.06);
    --photo-team-a: #bcd9ea;
    --photo-team-b: #5d93c9;
    --photo-baby-a: #f1d2bf;
    --photo-baby-b: #c99a82;
  }
  * { box-sizing: border-box; margin: 0; padding: 0; }
  html, body {
    width: 1200px; height: 982px; overflow: hidden;
    background: var(--page-bg);
    font-family: "Lato", Arial, sans-serif;
  }
  .brochure {
    position: absolute; left: 75px; top: 86px;
    width: 1050px; height: 810px;
    display: flex;
    background: var(--paper);
    box-shadow: 0 10px 30px rgba(0,0,0,0.18);
  }
  .panel {
    position: relative; width: 350px; height: 100%;
    overflow: hidden;
  }
  .panel + .panel { border-left: 1px solid var(--fold-shade); }
  .panel-art { position: absolute; left: 0; top: 0; display: block; }

  /* Left panel */
  .intro-copy {
    position: absolute; left: 38px; right: 34px; top: 336px;
  }
  .intro-heading {
    color: var(--brand-blue); font-weight: 700; font-size: 22px;
    margin-bottom: 8px;
  }
  .intro-body {
    color: var(--text-grey); font-size: 13px; line-height: 1.45;
    text-align: justify;
  }

  /* Brand lockup */
  .brand {
    display: flex; align-items: center; gap: 10px;
    color: var(--brand-blue); font-weight: 700;
  }
  .brand-dot {
    width: 22px; height: 22px; border-radius: 50%;
    background: var(--brand-blue); flex: none;
  }
  .brand-name { font-size: 46px; line-height: 0.95; letter-spacing: -0.5px; }
  .brand-sub { display: block; font-size: 15px; letter-spacing: 2.4px; text-transform: uppercase; margin-top: 4px; }

  /* Middle panel */
  .middle .brand { position: absolute; left: 44px; top: 228px; }
  .contact { position: absolute; left: 44px; right: 30px; top: 420px; }
  .contact-call {
    color: var(--brand-blue); font-weight: 900; font-size: 36px; line-height: 1;
  }
  .contact-phone {
    color: var(--brand-orange); font-weight: 700; font-size: 34px; line-height: 1.1;
    margin-bottom: 14px;
  }
  .contact-address {
    color: var(--text-grey); font-size: 15px; line-height: 1.35; font-style: normal;
  }
  .web-band {
    position: absolute; left: 0; right: 0; bottom: 0; height: 78px;
    background: var(--brand-orange);
    border-top: 5px solid var(--band-blue);
    display: flex; align-items: center; justify-content: center;
    color: #fff; font-weight: 700; font-size: 23px;
  }

  /* Right panel */
  .tagline {
    position: absolute; left: 0; right: 0; top: 466px;
    text-align: center; font-weight: 300; font-size: 42px; line-height: 1.02;
    color: var(--brand-blue); text-transform: uppercase;
  }
  .tagline .accent { color: var(--brand-orange); font-weight: 700; }
  .cover .brand { position: absolute; left: 46px; top: 656px; }
</style>
</head>
<body>
  <main class="brochure">

    <section class="panel inside-flap">
      <svg class="panel-art" width="350" height="330" viewBox="0 0 350 330">
        <defs>
          <linearGradient id="teamPhoto" x1="0" y1="0" x2="1" y2="1">
            <stop offset="0" stop-color="var(--photo-team-a)"/>
            <stop offset="1" stop-color="var(--photo-team-b)"/>
          </linearGradient>
        </defs>
        <path d="M0,262 Q175,318 350,262 V300 Q175,338 0,300 Z" fill="var(--band-light)"/>
        <path d="M0,282 Q175,338 350,282" fill="none" stroke="var(--band-blue)" stroke-width="9"/>
        <path d="M0,0 H350 V258 Q175,312 0,258 Z" fill="url(#teamPhoto)" role="img" aria-label="Photo of a smiling medical team in white coats and scrubs"/>
      </svg>
      <div class="intro-copy">
        <h2 class="intro-heading">Semper non enim</h2>
        <p class="intro-body">Proin ut magna id metus ornare dapibus condimentum ac est. Cras mi magna, venenatis sit amet pharetra in, pellentesque in orci. Mauris diam mi, semper non enim eleifend, mollis molestie tortor. Curabitur a mollis ante. Proin ut suscipit massa. Nullam sit amet tellus sollicitudin, tempus ligula eu.</p>
      </div>
    </section>

    <section class="panel middle">
      <div class="brand">
        <span class="brand-dot"></span>
        <span class="brand-name">vorantiq<span class="brand-sub">Medical Products</span></span>
      </div>
      <div class="contact">
        <p class="contact-call">CALL TODAY</p>
        <p class="contact-phone">877-555-0148</p>
        <address class="contact-address">14 Linden Road, Suite 200<br>Riverton, MA 01920</address>
      </div>
      <div class="web-band">www.vorantiq.com</div>
    </section>

    <section class="panel cover">
      <svg class="panel-art" width="350" height="440" viewBox="0 0 350 440">
        <defs>
          <linearGradient id="babyPhoto" x1="0" y1="0" x2="1" y2="1">
            <stop offset="0" stop-color="var(--photo-baby-a)"/>
            <stop offset="1" stop-color="var(--photo-baby-b)"/>
          </linearGradient>
        </defs>
        <path d="M0,330 Q175,410 350,350 V392 Q175,448 0,372 Z" fill="var(--band-light)"/>
        <path d="M0,350 Q175,430 350,370" fill="none" stroke="var(--band-blue)" stroke-width="10"/>
        <path d="M0,0 H350 V340 Q175,398 0,326 Z" fill="url(#babyPhoto)" role="img" aria-label="Close-up photo of a newborn's feet held in a parent's hands"/>
      </svg>
      <h1 class="tagline">We <span class="accent">Care</span><br>What<br><span class="accent">You Love</span></h1>
      <div class="brand">
        <span class="brand-dot"></span>
        <span class="brand-name">vorantiq<span class="brand-sub">Medical Products</span></span>
      </div>
    </section>

  </main>
</body>
</html>
```